Invoice design

Please design an invoice like the attached

- Please include a logo in the header (any logo rectangular is fine)

- We do not need a DUE DATE on the invoice (next to the total inc. vat)

- For each product put in smaller text beneath which might contain additional information about the product (e.g. size, colour choices)

- Do not put a signature in the footer

```html
<!DOCTYPE html>
<html lang="en">
<head>
<meta charset="utf-8">
<title>Invoice 00001 – Halden Ltd</title>
<link href="https://fonts.googleapis.com/css2?family=Jost:wght@300;400;500&family=Montserrat:wght@400;500;600&display=swap" rel="stylesheet">
<style>
:root{
  --accent:#b39480;
  --ink:#333333;
  --paper:#ffffff;
  --footer-bg:#e6e5e4;
  --footer-rule:#c4c4c0;
}
*{margin:0;padding:0;box-sizing:border-box}
html,body{width:813px;height:1200px;overflow:hidden;background:var(--paper)}
body{position:relative;font-family:"Montserrat",sans-serif;color:var(--ink)}
.abs{position:absolute;line-height:1;white-space:nowrap}
.top-band{position:absolute;left:0;top:0;width:813px;height:20px;background:var(--accent)}
.brand{position:absolute;left:592px;top:62px;width:148px;height:38px;display:flex;align-items:center;justify-content:center;gap:7px}
.brand-mark{width:11px;height:11px;background:var(--accent)}
.brand-name{font-family:"Jost",sans-serif;font-weight:500;font-size:21px;color:var(--ink);letter-spacing:.5px}
.doc-title{left:66px;top:108px;font-family:"Jost",sans-serif;font-weight:400;font-size:46px;color:var(--accent);letter-spacing:0}
.label{font-family:"Jost",sans-serif;font-size:13px;color:var(--accent);letter-spacing:.3px}
.meta-value{font-family:"Jost",sans-serif;font-size:14px;color:var(--ink)}
.divider{position:absolute;left:310px;top:107px;width:2px;height:296px;background:var(--accent)}
.party{font-size:11px}
.party.strong{font-weight:600}
.th{font-family:"Jost",sans-serif;font-size:15px;color:var(--accent)}
.rule{position:absolute;height:1px;background:var(--accent)}
.rule.thick{height:2px}
.item-name{font-size:12px;font-weight:500}
.item-note{font-size:7px;font-weight:500}
.cell{font-size:11px;font-weight:500}
.r{text-align:right}
.sum-label{font-family:"Jost",sans-serif;font-size:13px;color:var(--accent)}
.sum-value{font-size:14px;font-weight:500}
.total-box{position:absolute;left:68px;top:761px;width:678px;height:60px;border:1.5px dashed var(--accent)}
.total-amount{font-family:"Jost",sans-serif;font-weight:500;font-size:27px;color:var(--accent)}
.footer{position:absolute;left:0;top:859px;width:813px;height:341px;background:var(--footer-bg)}
.footer-notch{position:absolute;left:393px;top:859px}
.thanks{font-size:12px;font-weight:500}
.pay-divider{position:absolute;left:568px;top:909px;width:1px;height:142px;background:var(--footer-rule)}
.pay-value{font-size:12px;font-weight:500}
.footer-rule{position:absolute;left:68px;top:1096px;width:678px;height:1px;background:var(--footer-rule)}
.contact{left:0;width:813px;text-align:center;font-size:10px;font-weight:500}
.contact .sep{margin:0 8px}
</style>
</head>
<body>
<div class="top-band"></div>

<div class="brand"><span class="brand-mark"></span><span class="brand-name">HALDEN LTD</span></div>

<h1 class="abs doc-title">INVOICE</h1>

<div class="abs label" style="left:68px;top:181px">INVOICE:</div>
<div class="abs meta-value" style="left:68px;top:199px">00001</div>
<div class="abs label" style="left:68px;top:230px">ISSUE DATE:</div>
<div class="abs meta-value" style="left:68px;top:249px">July 3, 2020</div>
<div class="abs label" style="left:68px;top:280px">DELIVERY DATE:</div>
<div class="abs meta-value" style="left:68px;top:299px">July 3, 2020</div>

<div class="divider"></div>

<div class="abs label" style="left:338px;top:111px">SUPPLIER</div>
<div class="abs party strong" style="left:338px;top:129px">Halden Ltd</div>
<div class="abs party" style="left:338px;top:147px">42 Larch Street</div>
<div class="abs party" style="left:338px;top:165px">London</div>
<div class="abs party" style="left:338px;top:184px">EC1V 4QR</div>
<div class="abs party" style="left:338px;top:201px">United Kingdom</div>
<div class="abs party" style="left:338px;top:219px">VAT No: GB4410382276</div>

<div class="abs label" style="left:338px;top:263px">CLIENT</div>
<div class="abs party strong" style="left:338px;top:282px">Martin Hale</div>
<div class="abs party strong" style="left:338px;top:300px">The Copper Kettle</div>
<div class="abs party" style="left:338px;top:318px">18 Orchard Lane</div>
<div class="abs party" style="left:338px;top:336px">London</div>
<div class="abs party" style="left:338px;top:354px">NW3 7QT</div>
<div class="abs party" style="left:338px;top:372px">United Kingdom</div>
<div class="abs party" style="left:338px;top:390px">VAT No: GB987 6543 21</div>

<div class="abs th" style="left:68px;top:478px">Item</div>
<div class="abs th" style="left:293px;top:478px">Description</div>
<div class="abs th" style="left:403px;top:478px">Quantity</div>
<div class="abs th r" style="right:180px;top:478px">Unit Price incl. VAT</div>
<div class="abs th r" style="right:132px;top:478px">VAT</div>
<div class="abs th r" style="right:67px;top:478px">Total</div>
<div class="rule thick" style="left:68px;top:505px;width:678px"></div>

<div class="abs item-name" style="left:68px;top:523px">Highland Ridge Blend</div>
<div class="abs item-note" style="left:68px;top:537px">35Kg | White</div>
<div class="abs cell" style="left:292px;top:524px">1 kg / Full City</div>
<div class="abs cell" style="left:428px;top:524px">2</div>
<div class="abs cell r" style="right:180px;top:524px">15.00</div>
<div class="abs cell r" style="right:132px;top:524px">20%</div>
<div class="abs cell r" style="right:68px;top:524px">£30.00</div>
<div class="rule" style="left:68px;top:550px;width:678px"></div>

<div class="abs item-name" style="left:68px;top:566px">Valle Verde - La Rosa</div>
<div class="abs item-note" style="left:68px;top:580px">52kg | Brown</div>
<div class="abs cell" style="left:292px;top:567px">1 kg / Full City</div>
<div class="abs cell" style="left:428px;top:567px">3</div>
<div class="abs cell r" style="right:180px;top:567px">65.00</div>
<div class="abs cell r" style="right:132px;top:567px">20%</div>
<div class="abs cell r" style="right:68px;top:567px">£195.00</div>
<div class="rule" style="left:68px;top:592px;width:678px"></div>

<div class="abs sum-label" style="left:434px;top:610px">SUBTOTAL:</div>
<div class="abs sum-value r" style="right:67px;top:609px">£225.00</div>
<div class="rule" style="left:429px;top:637px;width:317px"></div>
<div class="abs sum-label" style="left:434px;top:652px">SHIPPING:</div>
<div class="abs sum-value r" style="right:67px;top:651px">£18.00</div>
<div class="rule" style="left:429px;top:679px;width:317px"></div>
<div class="abs sum-label" style="left:434px;top:693px">TOTAL EXCL. VAT:</div>
<div class="abs sum-value r" style="right:67px;top:692px">£205.00</div>
<div class="rule" style="left:429px;top:720px;width:317px"></div>
<div class="abs sum-label" style="left:434px;top:734px">VAT 20%:</div>
<div class="abs sum-value r" style="right:67px;top:733px">£37.50</div>

<div class="total-box"></div>
<div class="abs sum-label" style="left:434px;top:786px">TOTAL INCL. VAT:</div>
<div class="abs total-amount r" style="right:94px;top:778px">£243.00</div>

<div class="footer"></div>
<svg class="footer-notch" width="28" height="15" viewBox="0 0 28 15" aria-hidden="true"><polygon points="0,0 28,0 14,14" fill="#ffffff"/></svg>

<div class="abs thanks" style="left:68px;top:913px">Thank you for your purchase.</div>

<div class="pay-divider"></div>
<div class="abs label" style="left:597px;top:913px">PAYMENT METHOD</div>
<div class="abs pay-value" style="left:597px;top:933px">Bank Transfer</div>
<div class="abs label" style="left:597px;top:965px">BANK ACCOUNT</div>
<div class="abs pay-value" style="left:597px;top:985px">4400 0000 0192 3365</div>
<div class="abs label" style="left:597px;top:1015px">ORDER NUMBER</div>
<div class="abs pay-value" style="left:597px;top:1035px">#1029</div>

<div class="footer-rule"></div>
<div class="abs contact" style="top:1117px">Halden Ltd<span class="sep">|</span>Phone: +44 1632 960555<span class="sep">|</span>Email: hello@halden.co.uk<span class="sep">|</span>Website: halden.co.uk<span class="sep">|</span>Twitter: twitter.com/haldenltd</div>
<div class="abs contact" style="top:1144px">View this document online at https://docs.halden.co.uk/inv7k2m9p. Created in Ledgerly.</div>
</body>
</html>
```